Business card design needed

I run a life coaching business.
I coach individuals, businesses & groups.
Our aim is create massive change for our clients.
I would like to see a card that is inspirational, something that provokes the thought of achieving your personal best.
Be your own inspiration is a phrase I am considering using.

Target Market(s)

People who are looking to create a massive change in their lives.

Industry/Entity Type

Life Coaching

Contact Information for Business Card

Summit Stride Coaching
Neil Corbett
Head Coach
email neil@velomira.com.au
Mob 0412 583 604

Logo styles of interest
Abstract Logo
Requirements
Must have
• I wouldlike to have a free introductory offer on the reverse side of the card.
It would read something like:
Is coaching for me/you?
Try a free 45 minute session.
Book now call or email for your appointment.

```html
<!DOCTYPE html>
<html lang="en">
<head>
<meta charset="utf-8">
<title>Summit Stride Coaching – Business Card</title>
<link rel="stylesheet" href="https://fonts.googleapis.com/css2?family=Montserrat:wght@600&family=Questrial&family=Arimo:wght@700&display=swap">
<style>
  :root {
    --orange: #ef7f1a;
    --charcoal: #2d2a2a;
    --ink: #333333;
    --paper: #ffffff;
    --backdrop: #e9e9e9;
    --figure-light: #e4e4e4;
    --figure-mid: #cfcfcf;
  }
  * { margin: 0; padding: 0; box-sizing: border-box; }
  html, body {
    width: 994px;
    height: 1200px;
    overflow: hidden;
    background: var(--backdrop);
  }
  .canvas {
    position: relative;
    width: 994px;
    height: 1200px;
  }
  .card {
    position: absolute;
    left: 105px;
    width: 803px;
    height: 459px;
    background: var(--paper);
    overflow: hidden;
    box-shadow: 0 6px 16px rgba(0, 0, 0, 0.18);
  }
  .card--front { top: 128px; }
  .card--back { top: 625px; }

  .block { position: absolute; }
  .block--orange { background: var(--orange); }
  .block--dark { background: var(--charcoal); }

  /* Front */
  .climbers {
    position: absolute;
    left: 369px;
    top: 27px;
    width: 434px;
    height: 339px;
    background: linear-gradient(160deg, var(--figure-light), var(--figure-mid));
  }
  .holder-name {
    position: absolute;
    left: 113px;
    top: 89px;
    font-family: "Montserrat", sans-serif;
    font-weight: 600;
    font-size: 40px;
    line-height: 1.05;
    color: var(--ink);
  }
  .holder-title {
    position: absolute;
    left: 113px;
    top: 143px;
    font-family: "Questrial", sans-serif;
    font-size: 33px;
    line-height: 1.05;
    color: var(--ink);
  }
  .contact {
    position: absolute;
    left: 113px;
    font-family: "Questrial", sans-serif;
    font-size: 29px;
    line-height: 1.05;
    color: var(--ink);
  }
  .contact--phone { top: 214px; }
  .contact--email { top: 257px; }
  .contact-icon { position: absolute; }
  .contact-icon--phone { left: 62px; top: 213px; width: 30px; height: 34px; }
  .contact-icon--email { left: 60px; top: 262px; width: 38px; height: 24px; }

  .business-name {
    position: absolute;
    left: 33px;
    top: 386px;
    font-family: "Arimo", sans-serif;
    font-weight: 700;
    font-size: 48px;
    line-height: 1;
    color: var(--paper);
    white-space: nowrap;
    text-shadow: 3px 3px 0 var(--charcoal);
  }

  /* Back */
  .offer-heading {
    position: absolute;
    left: 0;
    width: 803px;
    top: 76px;
    text-align: center;
    font-family: "Arimo", sans-serif;
    font-weight: 700;
    font-size: 42px;
    line-height: 1;
    color: var(--orange);
    text-shadow: 2px 2px 0 #8a8a8a;
  }
  .offer-line {
    position: absolute;
    font-family: "Arimo", sans-serif;
    font-weight: 700;
    line-height: 1;
    color: var(--charcoal);
    white-space: nowrap;
  }
  .offer-line--trial { left: 203px; top: 191px; font-size: 28px; }
  .offer-line--booking { left: 181px; top: 306px; font-size: 25px; }
</style>
</head>
<body>
<main class="canvas">

  <section class="card card--front">
    <div class="climbers" role="img" aria-label="Illustration of two figures climbing steps, one reaching down to help the other up"></div>

    <div class="block block--orange" style="left:0; top:366px; width:527px; height:93px;"></div>
    <div class="block block--dark" style="left:527px; top:366px; width:276px; height:93px;"></div>
    <div class="block block--dark" style="left:663px; top:276px; width:140px; height:90px;"></div>
    <div class="block block--orange" style="left:527px; top:276px; width:136px; height:90px;"></div>
    <div class="block block--orange" style="left:663px; top:182px; width:140px; height:94px;"></div>

    <h1 class="holder-name">Neil Corbett</h1>
    <p class="holder-title">Head Coach</p>

    <svg class="contact-icon contact-icon--phone" viewBox="0 0 30 34" aria-hidden="true">
      <rect x="4" y="1.5" width="22" height="31" rx="3" fill="none" stroke="var(--orange)" stroke-width="2.5"/>
      <line x1="4" y1="26" x2="26" y2="26" stroke="var(--orange)" stroke-width="2"/>
      <line x1="12" y1="29.5" x2="18" y2="29.5" stroke="var(--orange)" stroke-width="1.5"/>
    </svg>
    <p class="contact contact--phone">0412 583 604</p>

    <svg class="contact-icon contact-icon--email" viewBox="0 0 38 24" aria-hidden="true">
      <rect x="1.5" y="1.5" width="35" height="21" fill="none" stroke="var(--orange)" stroke-width="2.5"/>
      <polyline points="1.5,1.5 19,14 36.5,1.5" fill="none" stroke="var(--orange)" stroke-width="2.5"/>
    </svg>
    <p class="contact contact--email">neil@velomira.com.au</p>

    <p class="business-name">SUMMIT STRIDE COACHING</p>
  </section>

  <section class="card card--back">
    <h2 class="offer-heading">IS COACHING FOR YOU?</h2>

    <div class="block block--orange" style="left:0; top:184px; width:139px; height:92px;"></div>
    <div class="block block--dark" style="left:0; top:276px; width:139px; height:183px;"></div>
    <div class="block block--orange" style="left:139px; top:276px; width:140px; height:93px;"></div>
    <div class="block block--dark" style="left:139px; top:369px; width:140px; height:90px;"></div>
    <div class="block block--orange" style="left:279px; top:369px; width:524px; height:90px;"></div>

    <p class="offer-line offer-line--trial">Try a free 45 minute session</p>
    <p class="offer-line offer-line--booking">Book now, call or email for your appointment</p>
  </section>

</main>
</body>
</html>
```